NEED BILLBOARDS FOR VELMORANCIA

we need to redo our billboards for our business. we want to have catchy, great billboards that follow standard billboard design rules. we do breast and body cosmetic surgery in Bakersfield, fresno, and stockton ca. see attached for some tips. i would like something creative, but conservative, but funny. we also won finest around 18 years in a row and can give you the logo

Target Market(s)

females 21-45

Industry/Entity Type

plastic surgery of the breast and body

Font styles to use
Serif

Requirements
Nice to have
• funny, catchy
Should not have
• pictures of women that are overly exposed

```html
<!DOCTYPE html>
<html lang="en">
<head>
<meta charset="utf-8">
<title>Velmorancia Billboard</title>
<link rel="stylesheet" href="https://fonts.googleapis.com/css2?family=Roboto+Serif:opsz,wdth,wght@8..144,50..150,400&display=swap">
<style>
  :root {
    --page-bg: #eef1f5;
    --board-bg: #ffffff;
    --headline: #4b5592;
    --brand-green: #8ccb8a;
    --brand-pink: #d98aa6;
    --glow: 244, 192, 143;
    --photo-warm: #b97c62;
    --photo-soft: #e4b8a2;
  }
  * { margin: 0; padding: 0; box-sizing: border-box; }
  html, body {
    width: 1200px;
    height: 1030px;
    overflow: hidden;
    background: var(--page-bg);
  }
  .billboard {
    position: absolute;
    left: 40px;
    top: 336px;
    width: 1120px;
    height: 358px;
    background: var(--board-bg);
    overflow: hidden;
    box-shadow: 0 4px 18px rgba(40, 50, 80, 0.18);
    font-family: "Roboto Serif", Georgia, serif;
  }
  .billboard__glow {
    position: absolute;
    left: 440px;
    top: 30px;
    width: 700px;
    height: 230px;
    background: radial-gradient(ellipse at 60% 45%, rgba(var(--glow), 0.75) 0%, rgba(var(--glow), 0.35) 45%, rgba(255, 255, 255, 0) 75%);
  }
  .billboard__photo {
    position: absolute;
    left: 0;
    top: 0;
    width: 480px;
    height: 358px;
    background: linear-gradient(90deg, var(--photo-warm) 0%, var(--photo-soft) 55%, rgba(255, 255, 255, 0) 100%);
  }
  .billboard__headline {
    position: absolute;
    left: 500px;
    top: 62px;
    font-family: "Roboto Serif", Georgia, serif;
    font-stretch: 80%;
    font-weight: 400;
    font-size: 64px;
    line-height: 74px;
    color: var(--headline);
    white-space: nowrap;
  }
  .brand {
    position: absolute;
    left: 543px;
    top: 262px;
  }
  .brand__name {
    font-size: 30px;
    line-height: 34px;
    font-weight: 400;
    font-stretch: 80%;
    color: var(--brand-green);
    letter-spacing: 0.5px;
  }
  .brand__tagline {
    font-size: 7.5px;
    font-stretch: 80%;
    color: var(--brand-pink);
    letter-spacing: 0.2px;
    margin-top: 2px;
  }
  .billboard__url {
    position: absolute;
    right: 38px;
    top: 288px;
    font-size: 26px;
    font-stretch: 80%;
    color: var(--headline);
  }
</style>
</head>
<body>
  <div class="billboard">
    <div class="billboard__glow"></div>
    <div class="billboard__photo" role="img" aria-label="Portrait photograph of a woman with long auburn hair"></div>
    <h1 class="billboard__headline">Your beauty secret<br>will be safe with us</h1>
    <div class="brand">
      <div class="brand__name">VELMORANCIA</div>
      <div class="brand__tagline">COSMETIC SURGERY AND MEDICAL AESTHETICS</div>
    </div>
    <div class="billboard__url">velmorancia.com</div>
  </div>
</body>
</html>
```